Lifestyle brand needs lip balm label design

We need a label design for lip balm tubes. The name of our company is "quorvalent"

Design Description:
Our lip balm tubes will be black. The label itself will be clear/transparent. We would like to create a gradient effect with the color green (same shade as our logo) starting from the bottom and slowly fading out to clear so that the black tube is visible (example of gradient shown in attached image)

We have two lip balm flavors: mint and lemongrass.
We would like the top/clear portion of the label to say "MINT" (all caps) . The second label should say "LEMONGRASS" (all caps) in the same location. Our logo "quorvalent" should be in the bottom/green portion of the label. Below the logo, we would like the words "NATURAL BALM" (all caps) in white text

```html
<!DOCTYPE html>
<html lang="en">
<head>
<meta charset="UTF-8">
<title>quorvalent Natural Balm – Mint label</title>
<link rel="stylesheet" href="https://fonts.googleapis.com/css2?family=Jost:wght@300;400&display=swap">
<style>
  :root {
    --page-bg: #ffffff;
    --leaf-green: #61974a;
    --mid-green: #5e7b51;
    --shadow-green: #3b4239;
    --tube-black: #000000;
    --text-white: #ffffff;
  }
  * { margin: 0; padding: 0; box-sizing: border-box; }
  html, body {
    width: 908px;
    height: 1200px;
    overflow: hidden;
    background: var(--page-bg);
  }
  body {
    font-family: "Jost", "Futura", sans-serif;
    display: flex;
    align-items: center;
    justify-content: center;
  }
  .balm-label {
    position: relative;
    width: 808px;
    height: 856px;
    background: linear-gradient(
      to top,
      var(--leaf-green) 0%,
      var(--leaf-green) 40%,
      var(--mid-green) 52%,
      var(--shadow-green) 60%,
      var(--tube-black) 66%,
      var(--tube-black) 100%
    );
    color: var(--text-white);
    text-align: center;
  }
  .flavour-art {
    position: absolute;
    left: 350px;
    top: 140px;
    width: 108px;
    height: 108px;
    border-radius: 50%;
    background: radial-gradient(circle, rgba(255,255,255,0.2) 0%, rgba(255,255,255,0.06) 70%, rgba(255,255,255,0) 100%);
  }
  .flavour-name {
    position: absolute;
    left: 0;
    right: 0;
    top: 282px;
    font-weight: 300;
    font-size: 76px;
    line-height: 1;
    letter-spacing: 6px;
    text-transform: uppercase;
  }
  .brand-name {
    position: absolute;
    left: 0;
    right: 0;
    top: 560px;
    font-weight: 400;
    font-size: 72px;
    line-height: 1;
    letter-spacing: 0.5px;
    color: var(--text-white);
  }
  .product-type {
    position: absolute;
    left: 0;
    right: 0;
    top: 644px;
    font-weight: 300;
    font-size: 44px;
    line-height: 1;
    letter-spacing: 4px;
    text-transform: uppercase;
    color: var(--text-white);
  }
  .divider {
    position: absolute;
    left: 320px;
    top: 712px;
    width: 168px;
    height: 2px;
    background: var(--text-white);
  }
  .tagline {
    position: absolute;
    left: 0;
    right: 0;
    top: 734px;
    font-weight: 400;
    font-size: 18.5px;
    line-height: 27px;
    letter-spacing: 0.3px;
  }
</style>
</head>
<body>
  <section class="balm-label">
    <div class="flavour-art" role="img" aria-label="Line drawing of mint leaves"></div>
    <h1 class="flavour-name">Mint</h1>
    <p class="brand-name">quorvalent</p>
    <p class="product-type">Natural Balm</p>
    <div class="divider"></div>
    <p class="tagline">Lorem ipsum dolor sit amet, consectetuer<br>adipiscing elit, sed diam nonummy nibh</p>
  </section>
</body>
</html>
```